Plakat-Design für Bühnenshow
Zielgruppe
Das Plakat soll folgende Bühnenshow vermarkten / The poster should promote the following stage show.
True-Crime Bühnenprogramm on Tour
Wo Sätze lauern
Spuren hinter jedem Komma
mit Ex-Geheimagent Bernd Quast
Haben Sie sich schon einmal gefragt, was Ihre Sprache alles über Sie verrät? Wenn Worte zu Waffen und Texte zu Tatorten werden startet ihr Einsatz: Bernd Quast und Florian Weidach sind Sprachprofiler. Auf ihrem sprachwissenschaftlichen Seziertisch landen Drohbriefe, Erpresserschreiben, aber auch ganz gewöhnliche Morddrohungen. Im Auftrag von Sicherheitsbehörden und Betroffenen überführen sie anonyme Täter alleine anhand deren Sprachmuster. Das Bühnenprogramm „Wo Sätze lauern – Spuren hinter jedem Komma“ gibt Ihnen einen tiefen Einblick in die Welt der forensischen Linguistik. Sie haben die Chance die Arbeit der Sprachprofiler kennenzulernen und zu erfahren, wie man sprachliche Profile erstellt, um Verbrechen aufzudecken. Überraschend, unterhaltsam – und spannender als die Polizei erlaubt! Besuchen Sie unsere Webseite www.wortfahnder-info.de und sichern Sie sich jetzt Ihre Tickets für ein unvergessliches Erlebnis!
True Crime Stageprogram
Where clauses lurk
Traces behind every comma
with former secret service agent Bernd Quast
Have you ever wondered what your language reveals about you? When words become weapons and texts become crime scenes, it's time for their intervention: Bernd Quast and Florian Weidach are profilers. Threatening letters, extortion letters, but also ordinary death threats land on their language science dissecting table. On behalf of security authorities and affected persons, they convict anonymous offenders solely on the basis of their language patterns. The stage program 'Where clauses lurk - Traces behind every comma' gives you a deep insight into the world of forensic linguistics. You have the chance to get to know the work of language profilers an..
Aufgabenstellung
Das Plakat soll o. g. Bühnenprogramm vermarkten. / The poster should promote the stage show.

```html
<!DOCTYPE html>
<html lang="de">
<head>
<meta charset="utf-8">
<title>Wo Sätze lauern – True-Crime Bühnenprogramm</title>
<link rel="stylesheet" href="https://fonts.googleapis.com/css2?family=Rubik+Dirt&family=Archivo+Black&family=Roboto+Condensed:wght@700&display=swap">
<style>
  :root {
    --bg-deep: #0b0f14;
    --bg-mid: #1a2129;
    --type-light: #f2f4f5;
    --badge-red: #a81c12;
    --badge-text: #f4ece8;
    --photo-dark: #121820;
    --photo-mid: #2c3640;
  }
  * { margin: 0; padding: 0; box-sizing: border-box; }
  html, body { width: 856px; height: 1200px; overflow: hidden; background: var(--bg-deep); }
  .poster {
    position: relative;
    width: 856px;
    height: 1200px;
    overflow: hidden;
    background: radial-gradient(ellipse at 50% 40%, var(--bg-mid) 0%, var(--bg-deep) 75%);
    color: var(--type-light);
  }
  .type-texture {
    position: absolute; inset: 0;
    background: linear-gradient(160deg, #1c232b 0%, #11161c 50%, #0a0d11 100%);
    opacity: .8;
  }
  .tagline {
    position: absolute; top: 48px; left: 0; width: 100%;
    text-align: center;
    font-family: "Archivo Black", sans-serif;
    font-size: 29px; letter-spacing: 1px;
  }
  .title {
    position: absolute; left: 0; width: 100%;
    text-align: center;
    font-family: "Rubik Dirt", sans-serif;
    font-size: 150px; line-height: 1;
    letter-spacing: 2px;
  }
  .title--one { top: 105px; }
  .title--two { top: 262px; }
  .title--three { top: 423px; }
  .subtitle {
    position: absolute; left: 330px; width: 420px; top: 596px;
    text-align: center;
    font-family: "Archivo Black", sans-serif;
    font-size: 29px; line-height: 1.25; letter-spacing: 1px;
  }
  .hosts-photo {
    position: absolute; left: 188px; top: 705px; width: 490px; height: 495px;
    background: radial-gradient(ellipse at 50% 40%, var(--photo-mid) 0%, var(--photo-dark) 60%, transparent 100%);
  }
  .badge {
    position: absolute; left: 32px; top: 526px; width: 284px; height: 284px;
    border-radius: 50%;
    background: var(--badge-red);
    box-shadow: 0 6px 18px rgba(0,0,0,.5);
  }
  .badge__text {
    position: absolute; inset: 0;
    display: flex; flex-direction: column; justify-content: center; align-items: center;
    transform: rotate(-14deg);
    font-family: "Archivo Black", sans-serif;
    font-size: 27px; line-height: 1.2; color: var(--badge-text);
    text-align: center;
  }
  .tickets {
    position: absolute; top: 1060px; left: 0; width: 100%;
    text-align: center;
    font-family: "Roboto Condensed", sans-serif; font-weight: 700;
    font-size: 27px;
  }
  .website {
    position: absolute; top: 1100px; left: 0; width: 100%;
    text-align: center;
    font-family: "Archivo Black", sans-serif;
    font-size: 30px; letter-spacing: 1px;
  }
</style>
</head>
<body>
<main class="poster">
  <div class="type-texture" role="img" aria-label="Dunkler Hintergrund aus verstreuten Bleisatz-Lettern"></div>

  <p class="tagline">TRUE-CRIME BÜHNENPROGRAMM ON TOUR</p>

  <h1>
    <span class="title title--one">WO</span>
    <span class="title title--two">SÄTZE</span>
    <span class="title title--three">LAUERN</span>
  </h1>

  <p class="subtitle">SPUREN HINTER JEDEM<br>KOMMA</p>

  <div class="hosts-photo" role="img" aria-label="Porträtfoto der beiden Sprachprofiler Bernd Quast und Florian Weidach in dunkler Kleidung"></div>

  <div class="badge">
    <p class="badge__text">MIT EX-<br>GEHEIMAGENT<br>BERND QUAST</p>
  </div>

  <p class="tickets">Tickets unter:</p>
  <p class="website">WWW.WORTFAHNDER-INFO.DE</p>
</main>
</body>
</html>
```